Travel Blogger Business Card for roamquill.net

I need a two-sided business card for a travel blogging website. The card should be both professional and fun at the same time. This is for the website www.roamquill.net

I don't necessarily think that the current logo on the website needs to be used on the business card but it can be. I am very flexible with ideas

Target Market(s)

Travel agencies that will be met at a conference.

Industry/Entity Type

Travel

Contact Information for Business Card

Company Name: Roam Quill.net
Name: Bertrand Olesky
Voice: +1-(345)-402-7731
Address: Coral Reach Shore, Grand Cayman, Cayman Islands
Email: ceo@roamquill.net

Colors
0592cd
0355a3
3176b5
33a6d7
85cae6
85acd3

Requirements
Must have
• Website address and name should be bigger than address, phone number, and email.

```html
<!DOCTYPE html>
<html lang="en">
<head>
<meta charset="utf-8">
<title>Roam Quill – Business Card</title>
<link rel="stylesheet" href="https://fonts.googleapis.com/css2?family=Roboto:wght@400;500;700;900&display=swap">
<style>
  :root {
    --page-bg: #5f6a72;
    --card-blue: #3176b5;
    --card-deep: #2a68a3;
    --accent-light: #85cae6;
    --accent-soft: #85acd3;
    --ink-white: #ffffff;
    --ink-muted: #d6e6f4;
    --rule: #85cae6;
  }
  * { box-sizing: border-box; margin: 0; padding: 0; }
  html, body { width: 1200px; height: 900px; overflow: hidden; }
  body {
    background: var(--page-bg);
    font-family: "Roboto", Arial, sans-serif;
    color: var(--ink-white);
    position: relative;
  }
  .card {
    position: absolute;
    left: 260px;
    width: 680px;
    height: 388px;
    background: var(--card-blue);
    overflow: hidden;
    box-shadow: 0 10px 30px rgba(0,0,0,0.35);
  }
  .card--front { top: 45px; }
  .card--back  { top: 467px; }

  /* front side */
  .front-decoration {
    position: absolute;
    inset: 40px 60px 40px 60px;
    border-radius: 190px;
    background: radial-gradient(ellipse at center, var(--card-deep) 0%, rgba(42,104,163,0.4) 60%, rgba(49,118,181,0) 80%);
  }
  .accent-bar {
    position: absolute;
    background: var(--accent-light);
    border-radius: 3px;
  }
  .accent-bar--top { left: 0; top: 0; width: 10px; height: 110px; }
  .accent-bar--bottom { right: 0; bottom: 0; width: 10px; height: 120px; }
  .front-brand {
    position: absolute;
    left: 0; right: 0; top: 150px;
    display: flex; align-items: center; justify-content: center; gap: 16px;
  }
  .brand-dot {
    width: 34px; height: 34px; border-radius: 50%;
    background: var(--ink-white);
  }
  .brand-name {
    font-weight: 900;
    font-size: 46px;
    letter-spacing: 1px;
    color: var(--ink-white);
  }
  .front-url {
    position: absolute;
    left: 0; right: 0; top: 300px;
    text-align: center;
    font-size: 17px;
    color: var(--ink-muted);
  }

  /* back side */
  .world-map {
    position: absolute;
    right: 0; top: 40px;
    width: 470px; height: 300px;
    background: radial-gradient(ellipse at 55% 50%, rgba(42,100,158,0.85) 0%, rgba(42,100,158,0.35) 55%, rgba(49,118,181,0) 75%);
  }
  .back-brand {
    position: absolute;
    right: 60px; top: 40px;
    display: flex; align-items: center; gap: 12px;
  }
  .back-brand .brand-dot { width: 24px; height: 24px; }
  .back-brand .brand-name { font-size: 30px; }
  .person {
    position: absolute;
    left: 50px; top: 120px;
  }
  .person-name { font-size: 28px; font-weight: 700; }
  .person-role { font-size: 13px; color: var(--ink-muted); letter-spacing: 1px; margin-top: 2px; }
  .person-rule { width: 290px; height: 2px; background: var(--rule); margin: 12px 0 12px; }
  .contact-line {
    display: flex; align-items: center; gap: 10px;
    font-size: 14px; color: var(--ink-muted); margin-bottom: 7px;
  }
  .contact-line svg { width: 14px; height: 14px; flex: none; }
  .company-info {
    position: absolute;
    right: 50px; bottom: 40px;
    text-align: right;
  }
  .company-url {
    display: flex; align-items: center; justify-content: flex-end; gap: 10px;
    font-size: 20px; font-weight: 500;
  }
  .company-url svg { width: 18px; height: 18px; }
  .company-rule { width: 320px; height: 2px; background: var(--rule); margin: 10px 0 10px auto; }
  .company-address { font-size: 14px; line-height: 1.45; color: var(--ink-muted); }
</style>
</head>
<body>

<section class="card card--front" aria-label="Card front">
  <div class="front-decoration" role="img" aria-label="Faint airplane illustration in a darker blue"></div>
  <span class="accent-bar accent-bar--top"></span>
  <span class="accent-bar accent-bar--bottom"></span>
  <div class="front-brand">
    <span class="brand-dot"></span>
    <span class="brand-name">ROAM QUILL</span>
  </div>
  <p class="front-url">www.roamquill.net</p>
</section>

<section class="card card--back" aria-label="Card back">
  <div class="world-map" role="img" aria-label="Faint world map in darker blue"></div>
  <div class="back-brand">
    <span class="brand-dot"></span>
    <span class="brand-name">ROAM QUILL</span>
  </div>
  <div class="person">
    <h1 class="person-name">Bertrand Olesky</h1>
    <p class="person-role">FOUNDER</p>
    <div class="person-rule"></div>
    <p class="contact-line">
      <svg viewBox="0 0 24 24" aria-hidden="true"><path fill="#ffffff" d="M6.6 10.8a15 15 0 0 0 6.6 6.6l2.2-2.2a1 1 0 0 1 1-.25 11.4 11.4 0 0 0 3.6.57 1 1 0 0 1 1 1V20a1 1 0 0 1-1 1A17 17 0 0 1 3 4a1 1 0 0 1 1-1h3.5a1 1 0 0 1 1 1c0 1.25.2 2.45.57 3.6a1 1 0 0 1-.25 1z"/></svg>
      +1-(345)-402-7731
    </p>
    <p class="contact-line">
      <svg viewBox="0 0 24 24" aria-hidden="true"><rect x="2" y="5" width="20" height="14" rx="2" fill="#ffffff"/><path d="M3 6l9 7 9-7" stroke="#3176b5" stroke-width="2" fill="none"/></svg>
      ceo@roamquill.net
    </p>
  </div>
  <div class="company-info">
    <p class="company-url">
      <svg viewBox="0 0 24 24" aria-hidden="true"><circle cx="12" cy="12" r="9" fill="none" stroke="#ffffff" stroke-width="2"/><path d="M3 12h18M12 3c3 3 3 15 0 18M12 3c-3 3-3 15 0 18" fill="none" stroke="#ffffff" stroke-width="1.5"/></svg>
      www.roamquill.net
    </p>
    <div class="company-rule"></div>
    <p class="company-address">Coral Reach Shore, Grand Cayman,<br>Cayman Islands</p>
  </div>
</section>

</body>
</html>
```